Logo für modernen Imbiss
Zielgruppe
Moderner Imbiss mit Diner Style
Aufgabenstellung
Da unser Lokal mit den Farben gelb, orange und schwarz gestaltet ist, wünschen wir uns auch diese Farben für unser Logo. Da wir eine Art 'Diner Style' repräsentieren, könnte das auch im Design der Speisekarte wiederzufinden sein. Wir sind aber sehr offen für eure Kreativität und haben erst einmal wenig Vorstellungen.

```html
<!DOCTYPE html>
<html lang="de">
<head>
<meta charset="utf-8">
<title>Mara's Kitchen – Speisekarte</title>
<link rel="stylesheet" href="https://fonts.googleapis.com/css2?family=Staatliches&family=Exo+2:ital,wght@1,300;1,700&display=swap">
<style>
:root{
  --orange:#f29100;
  --orange-deep:#d97f00;
  --ink:#262626;
  --cream:#ffffff;
  --paper:#ffffff;
}
*{box-sizing:border-box;margin:0;padding:0}
html,body{width:1200px;height:849px;overflow:hidden;background:var(--paper)}
.canvas{position:relative;width:1200px;height:849px}
.page{position:absolute;top:40px;width:542px;height:768px;background:var(--orange);color:var(--ink);overflow:hidden}
.page--cover{left:42px}
.page--menu{left:615px}
.illustration{position:absolute;left:118px;top:35px;width:306px;height:210px;border-radius:40px 40px 20px 20px;background:linear-gradient(180deg,var(--orange-deep),var(--orange))}
.brand{position:absolute;left:0;right:0;top:252px;text-align:center;font-family:"Staatliches",sans-serif;font-size:42px;letter-spacing:2px;color:var(--ink)}
.title{position:absolute;left:0;right:0;top:310px;text-align:center;font-family:"Staatliches",sans-serif;font-size:66px;letter-spacing:7px;line-height:1;color:var(--ink);font-weight:400}
.band{position:absolute;left:0;height:26px}
.band svg{position:absolute;left:0;top:0}
.band-shape{fill:var(--ink)}
.band span{position:absolute;left:17px;top:-1px;font-family:"Staatliches",sans-serif;font-size:26px;line-height:28px;letter-spacing:1.5px;color:var(--cream)}
.item{position:absolute;left:39px;right:39px}
.page--menu .item{left:38px;right:40px}
.item-name{font-family:"Staatliches",sans-serif;font-size:20px;line-height:20px;letter-spacing:1.5px}
.item-desc{font-family:"Exo 2",sans-serif;font-style:italic;font-weight:300;font-size:8.3px;line-height:9.5px;margin-top:1px}
.item-price{position:absolute;right:0;top:2px;font-family:"Staatliches",sans-serif;font-size:15px;letter-spacing:1.5px}
.item-price small{font-family:"Exo 2",sans-serif;font-style:italic;font-weight:300;font-size:8px;margin-right:3px;letter-spacing:0}
.or{font-size:13px}
.bubble{position:absolute}
.bubble-ring{fill:var(--ink)}
.bubble-fill{fill:var(--orange)}
.bubble-text{position:absolute;font-family:"Staatliches",sans-serif;color:var(--cream);text-align:center;line-height:1.15;letter-spacing:1px;white-space:nowrap}
.footer{position:absolute;left:0;right:0;bottom:0;height:51px;background:var(--ink);color:var(--cream);font-family:"Exo 2",sans-serif;font-style:italic;font-weight:700;font-size:9.5px;line-height:11px}
.footer-address{position:absolute;left:38px;top:11px}
.footer-hours{position:absolute;left:278px;top:11px;display:grid;grid-template-columns:91px 52px auto}
</style>
</head>
<body>
<div class="canvas">

  <section class="page page--cover">
    <div class="illustration" role="img" aria-label="Illustration einer Kellnerin im Diner-Stil mit Burger auf einem Tablett und Schriftband"></div>
    <div class="brand">Mara's Kitchen</div>
    <h1 class="title">Speisekarte</h1>

    <div class="band" style="top:409px;width:226px">
      <svg width="226" height="26" viewBox="0 0 226 26"><polygon class="band-shape" points="0,0 226,0 218,13 226,26 0,26"/></svg>
      <span>Frühstück</span>
    </div>

    <svg class="bubble" style="left:318px;top:403px" width="116" height="112" viewBox="0 0 116 112">
      <path class="bubble-ring" d="M58 6 C90 6 112 26 112 52 C112 66 104 78 94 86 L96 108 L80 92 C72 96 64 98 56 98 C26 98 4 80 4 52 C4 26 26 6 58 6 Z"/>
      <path class="bubble-fill" d="M58 15 C84 15 102 31 102 52 C102 64 96 74 86 80 L86 94 L78 86 C72 88 64 90 56 90 C32 90 13 75 13 52 C13 31 32 15 58 15 Z"/>
    </svg>
    <div class="bubble-text" style="left:329px;top:422px;width:94px;font-size:11.5px">Zu jedem<br>Frühstück:<br>Orangensaft<br>oder<br>Kaffee</div>

    <div class="item" style="top:444px"><div class="item-name">Belegtes Brötchen</div><div class="item-desc">wahlweise mit: Schinken, Käse oder Salami</div><div class="item-price">2,00 €</div></div>
    <div class="item" style="top:487px"><div class="item-name">Klassisch</div><div class="item-desc">2 Brötchen, Marmelade, Honig &amp; Butter</div><div class="item-price">4,00 €</div></div>
    <div class="item" style="top:529px"><div class="item-name">Handwerker</div><div class="item-desc">2 Brötchen, Salami, Schinken, Käse, 1 gekochtes Ei, Marmelade &amp; Butter</div><div class="item-price">6,00 €</div></div>
    <div class="item" style="top:572px"><div class="item-name">Business</div><div class="item-desc">2 Brötchen, verschiedene Käsesorten, 1 gekochtes Ei, Marmelade, Honig &amp; Butter</div><div class="item-price">6,00 €</div></div>
    <div class="item" style="top:614px"><div class="item-name">Geniesser</div><div class="item-desc">2 Brötchen, Verschiedene Käsesorten, Salami, Schinken, Lachs mit Meerrettich,<br>Rührei, Marmelade &amp; Butter</div><div class="item-price">8,00 €</div></div>
    <div class="item" style="top:665px"><div class="item-name">Amerikanisch</div><div class="item-desc">1 Brötchen, 2 Toasts, gebackene Bohnen, Würstchen, 2 Spiegeleier, Speck &amp; Butter</div><div class="item-price">8,00 €</div></div>

    <footer class="footer">
      <div class="footer-address">Mara's Kitchen<br>56481 Lindenau<br>Gewerbepark Nord</div>
      <div class="footer-hours">
        <span>Öffnungszeiten:</span><span>Mo.:<br>Di. - Sa.:</span><span>6:30 - 15:00 Uhr<br>6:30 - 19:00 Uhr<br>Sonntag Ruhetag</span>
      </div>
    </footer>
  </section>

  <section class="page page--menu">
    <div class="band" style="top:13px;width:226px">
      <svg width="226" height="26" viewBox="0 0 226 26"><polygon class="band-shape" points="0,0 226,0 218,13 226,26 0,26"/></svg>
      <span>Burger</span>
    </div>

    <svg class="bubble" style="left:268px;top:10px" width="164" height="100" viewBox="0 0 164 100">
      <path class="bubble-ring" d="M82 4 C128 4 160 20 160 42 C160 58 146 68 126 74 L132 96 L110 78 C101 80 92 80 82 80 C36 80 4 66 4 42 C4 20 36 4 82 4 Z"/>
      <path class="bubble-fill" d="M82 13 C122 13 150 26 150 42 C150 54 138 62 120 66 L120 80 L106 70 C98 71 90 71 82 71 C42 71 14 60 14 42 C14 26 42 13 82 13 Z"/>
    </svg>
    <div class="bubble-text" style="left:292px;top:33px;width:116px;font-size:9.5px;letter-spacing:0.8px;transform:rotate(-7deg)">Zu jedem Burger<br>gibt es verschiedene<br>Soßen!</div>

    <div class="item" style="top:53px"><div class="item-name">Classic Burger</div><div class="item-desc">Rindfleisch, Tomate, Gurken &amp; Salat</div><div class="item-price">5,50 €</div></div>
    <div class="item" style="top:93px"><div class="item-name">Cheese Burger</div><div class="item-desc">Rindfleisch, Käse, Tomaten, Gurken &amp; Salat</div><div class="item-price">5,80 €</div></div>
    <div class="item" style="top:134px"><div class="item-name">Handwerker Burger</div><div class="item-desc">Rindfleisch, Speck, Zwiebeln, Tomaten, Gurken &amp; Salat</div><div class="item-price">6,00 €</div></div>
    <div class="item" style="top:174px"><div class="item-name">Bauern Burger</div><div class="item-desc">Rindfleisch, Käse, Speck, Spiegelei, Tomaten, Gurken &amp; Salat</div><div class="item-price">6,50 €</div></div>
    <div class="item" style="top:215px"><div class="item-name">Fitness Burger</div><div class="item-desc">Putenbrust, Champignons, Tomaten, Gurken &amp; Salat</div><div class="item-price">6,50 €</div></div>
    <div class="item" style="top:255px"><div class="item-name">Veggie Burger</div><div class="item-desc">Gemüsepatty, Champignons, Zwiebeln, Tomaten, Gurke &amp; Salat</div><div class="item-price">6,00 €</div></div>

    <div class="band" style="top:297px;width:222px">
      <svg width="222" height="26" viewBox="0 0 222 26"><polygon class="band-shape" points="0,0 222,0 214,13 222,26 0,26"/></svg>
      <span>Klassiker</span>
    </div>

    <div class="item" style="top:334px"><div class="item-name">Bratwurst</div><div class="item-desc">im Brötchen</div><div class="item-price">2,50 €</div></div>
    <div class="item" style="top:375px"><div class="item-name">Currywurst</div><div class="item-desc">im Brötchen</div><div class="item-price">3,00 €</div></div>
    <div class="item" style="top:415px"><div class="item-name">Currywurst Spezial</div><div class="item-desc">mit Peperoni, Curry-Chilisoße &amp; Brötchen</div><div class="item-price">3,20 €</div></div>
    <div class="item" style="top:456px"><div class="item-name">Westerwälderwurst</div><div class="item-desc">mit Schmand-Kräutersoße, Zwiebeln, Speck &amp; Brötchen</div><div class="item-price">3,30 €</div></div>
    <div class="item" style="top:496px"><div class="item-name">Frikadelle</div><div class="item-desc">mit Brötchen</div><div class="item-price">2,30 €</div></div>
    <div class="item" style="top:537px"><div class="item-name">Frikadelle</div><div class="item-desc">mit Spiegelei, Speck, Zwiebeln &amp; Brötchen</div><div class="item-price">2,70 €</div></div>
    <div class="item" style="top:577px"><div class="item-name">Schnitzel</div><div class="item-desc">im Brötchen</div><div class="item-price">3,50 €</div></div>

    <div class="band" style="top:619px;width:222px">
      <svg width="222" height="26" viewBox="0 0 222 26"><polygon class="band-shape" points="0,0 222,0 214,13 222,26 0,26"/></svg>
      <span>Beilagen &amp; Soßen</span>
    </div>

    <div class="item" style="top:656px"><div class="item-name">Steakhouse Pommes, Curly-Fries,<br>Kartoffelecken <span class="or">oder</span> Beilagensalat</div><div class="item-desc">Als Beilage bei Wurst / Frikadelle / Burger je 1,20 €</div><div class="item-price"><small>je</small>2,00 €</div></div>
    <div class="item" style="top:714px"><div class="item-name">Soßen</div><div class="item-desc">Curry-, Rahm- oder Jägersoße</div><div class="item-price"><small>je</small>0,70 €</div></div>
  </section>

</div>
</body>
</html>
```